Business card design for new brand

We have recently rebranded and need a new business card template.

We are an insurance underwriting agency. All of our products are sold via other partner companies, so these are just to pass on our details to other organisations.

We would like to see designs that use the colour green (current stationary generally uses lime green (rgb 142,190,63) and forest green (0,154,79) to comply with our logo's colours. We are happy with other shades of green.

Business cards need to include our logo, as well as space for:
1. Full name
2. Qualifications (optional)
3. Title
4. Office number
5. Mobile number
6. Email address

Our logo is enclosed here.

```html
<!DOCTYPE html>
<html lang="en">
<head>
<meta charset="utf-8">
<title>Verdant Cover – Business Card</title>
<link rel="stylesheet" href="https://fonts.googleapis.com/css2?family=PT+Sans:wght@400;700&display=swap">
<style>
  :root {
    --page-bg: #dcdcdc;
    --forest: #009a4f;
    --forest-deep: #005a2d;
    --forest-mid: #007a3c;
    --lime: #8ebe3f;
    --citron: #d4d62a;
    --ink: #231f20;
    --white: #ffffff;
  }
  * { box-sizing: border-box; margin: 0; padding: 0; }
  html, body {
    width: 927px;
    height: 1200px;
    overflow: hidden;
    background: var(--page-bg);
    font-family: "PT Sans", sans-serif;
  }
  .card {
    position: absolute;
    left: 52px;
    width: 822px;
    height: 470px;
    overflow: hidden;
  }
  /* Front */
  .card--front {
    top: 103px;
    background: linear-gradient(90deg, #005e30 0%, #006b34 35%, var(--forest-mid) 60%, #008c48 100%);
    display: flex;
    align-items: center;
    justify-content: center;
  }
  .front-brand {
    display: flex;
    align-items: center;
    gap: 18px;
    color: var(--white);
    font-weight: 400;
  }
  .front-brand__mark {
    width: 40px;
    height: 40px;
    background: var(--lime);
    flex: none;
  }
  .front-brand__text { text-align: center; line-height: 1; }
  .front-brand__name {
    display: block;
    font-size: 54px;
    letter-spacing: -0.5px;
  }
  .front-brand__legal {
    display: block;
    margin-top: 8px;
    font-size: 28px;
  }
  /* Back */
  .card--back {
    top: 662px;
    background: var(--white);
    box-shadow: -6px 8px 14px rgba(0, 0, 0, 0.45);
  }
  .back-panel {
    position: absolute;
    inset: 0;
  }
  .back-brand {
    position: absolute;
    left: 31px;
    top: 172px;
    display: flex;
    align-items: center;
    gap: 14px;
    color: var(--ink);
  }
  .back-brand__mark {
    width: 34px;
    height: 34px;
    background: var(--forest);
    flex: none;
  }
  .back-brand__text { font-weight: 400; line-height: 1; }
  .back-brand__name { display: block; font-size: 46px; letter-spacing: -0.5px; }
  .back-brand__legal { display: block; font-size: 26px; margin-top: 6px; padding-left: 38px; }
  .person {
    position: absolute;
    left: 494px;
    top: 74px;
    width: 48px;
    height: 60px;
  }
  .identity {
    position: absolute;
    left: 563px;
    top: 70px;
    line-height: 1;
  }
  .identity__name {
    display: block;
    font-size: 33px;
    font-weight: 700;
    color: var(--citron);
  }
  .identity__title {
    display: block;
    margin-top: 6px;
    font-size: 26px;
    font-weight: 700;
    color: var(--white);
  }
  .contacts {
    position: absolute;
    right: 38px;
    top: 330px;
    list-style: none;
    color: var(--white);
    font-size: 21px;
  }
  .contacts li {
    display: flex;
    justify-content: flex-end;
    align-items: center;
    gap: 12px;
    height: 37px;
  }
  .contacts svg { width: 24px; height: 24px; flex: none; }
</style>
</head>
<body>

<section class="card card--front" aria-label="Card front">
  <div class="front-brand">
    <span class="front-brand__mark" aria-hidden="true"></span>
    <span class="front-brand__text">
      <span class="front-brand__name">Verdant Cover</span>
      <span class="front-brand__legal">Australia Pty Ltd</span>
    </span>
  </div>
</section>

<section class="card card--back" aria-label="Card back">
  <svg class="back-panel" viewBox="0 0 822 470" preserveAspectRatio="none" aria-hidden="true">
    <defs>
      <linearGradient id="panelGreen" x1="0" y1="0" x2="1" y2="0">
        <stop offset="0" stop-color="#009a4f"/>
        <stop offset="0.55" stop-color="#007a3c"/>
        <stop offset="0.92" stop-color="#005a2d"/>
        <stop offset="1" stop-color="#005a2d"/>
      </linearGradient>
    </defs>
    <path d="M309 0 H822 V470 H309 C360 385 385 310 385 220 C385 135 355 65 309 0 Z" fill="url(#panelGreen)"/>
  </svg>

  <div class="back-brand">
    <span class="back-brand__mark" aria-hidden="true"></span>
    <span class="back-brand__text">
      <span class="back-brand__name">Verdant Cover</span>
      <span class="back-brand__legal">Australia Pty Ltd</span>
    </span>
  </div>

  <svg class="person" viewBox="0 0 48 60" aria-hidden="true">
    <circle cx="24" cy="16" r="12" fill="none" stroke="#fff" stroke-width="4"/>
    <path d="M6 56 H42 Q46 56 46 52 V50 Q46 32 24 32 Q2 32 2 50 V52 Q2 56 6 56 Z" fill="none" stroke="#fff" stroke-width="4"/>
  </svg>

  <div class="identity">
    <span class="identity__name">Your Name</span>
    <span class="identity__title">Account Manager</span>
  </div>

  <ul class="contacts">
    <li>0200 555 010
      <svg viewBox="0 0 24 24" aria-hidden="true"><path d="M19 3 L22 6 C22 14 14 22 6 22 L3 19 L7 15 L10 17 C13 15 15 13 17 10 L15 7 Z" fill="#fff"/></svg>
    </li>
    <li>0400 555 020
      <svg viewBox="0 0 24 24" aria-hidden="true"><rect x="6" y="1" width="12" height="22" rx="2" fill="none" stroke="#fff" stroke-width="1.5"/><rect x="8.5" y="5" width="7" height="10" fill="#fff"/><circle cx="12" cy="19.5" r="1.2" fill="none" stroke="#fff"/></svg>
    </li>
    <li>info@verdantcover.com
      <svg viewBox="0 0 24 24" aria-hidden="true"><path d="M1 11 L23 2 L17 22 L11 14 Z M11 14 L23 2 M11 14 L11 20 L14 17" fill="none" stroke="#fff" stroke-width="1.2" stroke-linejoin="round"/></svg>
    </li>
  </ul>
</section>

</body>
</html>
```